Vantrisco website redesign

1.logo redesign
2. whole website lay out redesign
3. add more function and pages (have some detail in attachment).
4. design the info taking form layout(contact us, return request, trade pro, see all form in file)
5. also design the mobile look for the website
some reference website: https://www.plaquevora.example/
https://www.moskuden.example/

we want our website style between these two website, website should be user friendly focus + slight design style, and mobile one could more like https://www.moskuden.example/ (more design style)

Target Market(s)

Tile Ecommerce

Industry/Entity Type

Ecommerce, Tile

Coding

Coded - Design and coding required

Number of Pages Required

5+ page

```html
<!DOCTYPE html>
<html lang="en">
<head>
<meta charset="utf-8">
<title>Vantrisco – Mobile Website Screens</title>
<link rel="stylesheet" href="https://fonts.googleapis.com/css2?family=Poppins:wght@300;400;500;600;700&family=Open+Sans:wght@400;600&display=swap">
<style>
:root{
  --bg:#efe6fb;
  --card:#ffffff;
  --soft:#f5f5f5;
  --ink:#2f2f2f;
  --muted:#8a8a8a;
  --dark:#3b3b3b;
  --line:#555555;
  --photo-warm-a:#c9a27a;
  --photo-warm-b:#6e4a2d;
  --photo-tile-a:#d9dde6;
  --photo-tile-b:#3d5a86;
  --photo-room-a:#8b7a6c;
  --photo-room-b:#3f3630;
  --photo-kitchen-a:#d8b27c;
  --photo-kitchen-b:#6a1f2b;
}
*{box-sizing:border-box;margin:0;padding:0}
html,body{width:1200px;height:1200px;overflow:hidden}
body{background:var(--bg);font-family:"Open Sans",sans-serif;color:var(--ink);position:relative}
.brand{position:absolute;left:66px;top:128px;width:250px;white-space:nowrap;font-family:"Poppins",sans-serif;font-weight:300;font-size:44px;line-height:1;letter-spacing:.5px;color:var(--dark);z-index:2}
.screen{position:absolute;width:250px;background:var(--card);border-radius:16px;overflow:hidden;box-shadow:0 18px 40px rgba(90,60,140,.12)}
.pad{padding:18px 18px}
.title{font-family:"Poppins",sans-serif;font-weight:600;font-size:19px;line-height:1.2;text-align:center;color:var(--ink)}
.lead{font-size:8.5px;line-height:1.5;color:var(--muted);text-align:center;margin-top:8px}
.btn-outline{display:block;margin:12px auto 0;width:max-content;padding:5px 16px;border:1px solid var(--line);font-size:8.5px;color:var(--ink);background:#fff}
.btn-solid{display:block;margin:12px auto 0;width:max-content;padding:7px 22px;background:#fff;color:var(--ink);font-size:9px;font-family:"Poppins",sans-serif}
.btn-dark{display:block;margin:16px auto 0;width:max-content;padding:8px 26px;background:var(--dark);color:#fff;font-size:9px;letter-spacing:1.5px;font-family:"Poppins",sans-serif}
.photo{display:block;width:100%}
.photo-tile{background:linear-gradient(135deg,var(--photo-tile-a),var(--photo-tile-b) 120%)}
.photo-warm{background:linear-gradient(160deg,var(--photo-warm-a),var(--photo-warm-b))}
.photo-room{background:linear-gradient(170deg,var(--photo-room-a),var(--photo-room-b))}
.photo-kitchen{background:linear-gradient(150deg,var(--photo-kitchen-a),var(--photo-kitchen-b))}
.photo-grey{background:linear-gradient(160deg,#dadada,#7e7e7e)}
.photo-mono{background:linear-gradient(135deg,#e8e8e8,#555)}
.tag{font-family:"Poppins",sans-serif;font-weight:500;font-size:12px;text-align:center;background:#fff;margin:-14px auto 0;width:130px;padding:5px 0;position:relative}
.markets{display:flex;gap:8px;padding:0 12px 16px;margin-top:14px}
.market{flex:1;height:44px;background:var(--soft);display:flex;align-items:center;justify-content:center;font-family:"Poppins",sans-serif;font-size:11px;font-weight:500;color:#666}
.hero{position:relative;color:#fff;text-align:center}
.hero .shade{position:absolute;inset:0;background:rgba(0,0,0,.35)}
.hero .content{position:relative;padding:0 18px}
.hero h2{font-family:"Poppins",sans-serif;font-weight:600;font-size:18px;line-height:1.3}
.hero p{font-size:8px;line-height:1.6;margin-top:8px;opacity:.9}
.phone-bar{display:flex;justify-content:space-between;align-items:center;padding:14px 16px;position:relative}
.phone-bar .name{font-family:"Poppins",sans-serif;font-weight:400;font-size:13px;color:#fff}
.icons{display:flex;gap:9px}
.user{text-align:center;padding:18px}
.avatar{width:56px;height:56px;border-radius:8px;margin:0 auto 10px;background:linear-gradient(160deg,#b99a6c,#5b6b3c)}
.user h3{font-family:"Poppins",sans-serif;font-weight:600;font-size:15px}
.user small{font-size:8px;color:var(--muted)}
.user p{font-size:8.5px;line-height:1.6;color:#555;margin-top:8px}
.footer{background:var(--dark);color:#fff;text-align:center;padding:26px 18px}
.footer .name{font-family:"Poppins",sans-serif;font-weight:300;font-size:30px}
.footer .touch{font-family:"Poppins",sans-serif;font-size:11px;margin-top:12px}
.socials{display:flex;gap:10px;justify-content:center;margin-top:10px}
.socials span{width:18px;height:18px;border-radius:50%;background:#fff}
.collections{display:grid;grid-template-columns:1fr 1fr;gap:8px;margin-top:14px}
.coll h4{font-family:"Poppins",sans-serif;font-weight:600;font-size:10px;margin-top:6px}
.coll p{font-size:7px;line-height:1.5;color:var(--muted);margin-top:3px}
.coll .btn-outline{margin:6px 0 0;font-size:7.5px;padding:3px 10px}
.gallery-cap{text-align:center;padding:12px 18px 16px}
.gallery-cap h4{font-family:"Poppins",sans-serif;font-weight:500;font-size:12px}
.gallery-cap small{font-size:8px;color:var(--muted)}
</style>
</head>
<body>

<div class="brand">Vantrisco</div>

<!-- Column 1 -->
<section class="screen" style="left:40px;top:270px;">
  <div class="pad">
    <h2 class="title">New journey Starts Here</h2>
    <p class="lead">Lorem ipsum dolor sit amet, consectetur adipiscing elit ut aliquam</p>
  </div>
  <div class="photo photo-tile" style="height:250px" role="img" aria-label="Patterned blue and white encaustic tiles behind a wooden table with walnuts"></div>
  <div class="tag">Best Sellers</div>
  <p class="lead" style="padding:0 22px">Rorem ipsum dolor sit amet, consectetur adipiscing elit.Rorem</p>
  <span class="btn-outline">Read more</span>
  <div class="photo photo-mono" style="height:130px;margin-top:16px" role="img" aria-label="Black and white patterned floor tile close-up"></div>
</section>

<section class="screen" style="left:40px;top:900px;">
  <div class="photo photo-kitchen" style="height:120px" role="img" aria-label="Kitchen with burgundy wall tiles and copper kettle"></div>
  <div class="gallery-cap">
    <h4>Kitchen</h4>
    <small>@milolarkhaven</small>
    <span class="btn-outline">View All User Gallery</span>
  </div>
</section>

<!-- Column 2 -->
<section class="screen" style="left:330px;top:40px;">
  <div class="pad" style="padding-bottom:0"><h2 class="title">Marketplaces:</h2></div>
  <div class="markets">
    <div class="market">Arcadon</div><div class="market">Nestory</div><div class="market">Buildmart</div>
  </div>
  <div class="hero" style="height:260px;padding-top:46px">
    <div class="photo photo-warm" style="position:absolute;inset:0" role="img" aria-label="Tile sample boards with terrazzo and a eucalyptus sprig"></div>
    <div class="shade"></div>
    <div class="content">
      <h2>Create Your Dream Space - Shop Vantrisco Tiles</h2>
      <p>Yorem Ipsum Dolor Sit Amet, Consectetur Adipiscing Elit. Nunc Vulputate Libero Et Velit Interdum, Ac Aliquet Odio Mattis.</p>
      <span class="btn-solid">Contact Us</span>
    </div>
  </div>
  <div class="pad" style="background:var(--soft);padding:20px 18px 24px">
    <h2 class="title">What Customer say about Vantrisco</h2>
  </div>
</section>

<section class="screen" style="left:330px;top:560px;">
  <div class="photo photo-kitchen" style="height:110px" role="img" aria-label="Kitchen with burgundy wall tiles and copper kettle"></div>
  <div class="gallery-cap" style="background:var(--soft)">
    <h4>Kitchen</h4>
    <small>@milolarkhaven</small>
    <span class="btn-outline">View All User Gallery</span>
  </div>
  <div class="pad" style="padding-top:26px"><h2 class="title">Also Available On These Popular Marketplaces:</h2></div>
  <div class="markets">
    <div class="market">Arcadon</div><div class="market">Nestory</div><div class="market">Buildmart</div>
  </div>
  <div class="hero" style="height:130px;padding-top:40px">
    <div class="photo photo-warm" style="position:absolute;inset:0" role="img" aria-label="Tile sample boards with a eucalyptus sprig"></div>
    <div class="shade"></div>
    <div class="content"><h2>Create Your Dream</h2></div>
  </div>
</section>

<!-- Column 3 -->
<section class="screen" style="left:620px;top:40px;height:560px;background:var(--photo-room-b)">
  <div class="photo photo-room" style="position:absolute;inset:0" role="img" aria-label="Living room with framed mirror, grey sofa and rug"></div>
  <div class="hero" style="height:100%">
    <div class="shade" style="background:rgba(0,0,0,.18)"></div>
    <div class="phone-bar">
      <span class="name">Vantrisco</span>
      <span class="icons">
        <svg width="11" height="11" viewBox="0 0 12 12" fill="none" stroke="#fff" stroke-width="1.4"><circle cx="5" cy="5" r="3.8"/><path d="M8 8l3 3"/></svg>
        <svg width="12" height="11" viewBox="0 0 12 11" fill="none" stroke="#fff" stroke-width="1.3"><path d="M0.5 1h2l1.5 6h6.5l1-4.5H3"/><circle cx="5" cy="9.5" r=".8"/><circle cx="9.5" cy="9.5" r=".8"/></svg>
        <svg width="11" height="11" viewBox="0 0 12 12" fill="none" stroke="#fff" stroke-width="1.3"><circle cx="6" cy="4" r="2.6"/><path d="M1 11.5c.8-2.6 2.7-3.8 5-3.8s4.2 1.2 5 3.8"/></svg>
        <svg width="12" height="11" viewBox="0 0 12 11" stroke="#fff" stroke-width="1.4"><path d="M0 2h12M0 5.5h12M0 9h12"/></svg>
      </span>
    </div>
    <div class="content" style="padding-top:150px">
      <h2 style="font-size:21px">From Classic to Contemporary - Find Your Perfect Tile</h2>
      <p>Trusted by 100+ businesses across Hertfordshire, Essex, London and beyond. We deliver outstanding Managed IT Support, Cloud and Communications services.</p>
      <span class="btn-dark">Find Out More</span>
    </div>
  </div>
</section>

<section class="screen" style="left:620px;top:620px;">
  <div class="pad">
    <h2 class="title">Vantrisco Collections</h2>
    <p class="lead">Lorem ipsum dolor sit amet, consectetur adipiscing elit ut aliquam</p>
    <span class="btn-outline">View All Collections</span>
    <div class="collections">
      <div class="coll">
        <div class="photo photo-grey" style="height:200px" role="img" aria-label="Grey kitchen with glass subway tile backsplash"></div>
        <h4>Glass Collection</h4>
        <p>Known For Its Striking Sheen And Vivid, Long-Lasting Colors, Our Gloss Tile Brings A Luxurious Dimension.</p>
        <span class="btn-outline">Shop Now</span>
      </div>
      <div class="coll">
        <div class="photo photo-warm" style="height:200px" role="img" aria-label="Bathroom with ceramic tiles and arched mirror"></div>
        <h4>Ceramic Collection</h4>
        <p>Known For Its Striking Sheen And Vivid, Long-Lasting Colors, Our Tile Brings A Luxurious Dimension.</p>
        <span class="btn-outline">Shop Now</span>
      </div>
    </div>
  </div>
</section>

<!-- Column 4 -->
<section class="screen" style="left:910px;top:40px;">
  <div class="user">
    <div class="avatar" role="img" aria-label="Customer portrait"></div>
    <h3>Marisol</h3>
    <small>22 Years</small>
    <p>Borem ipsum dolor sit amet, consectetur adipiscing elit. Nunc vulputate libero et velit interdum, ac aliquet odio mattis. Class aptent taciti sociosqu ad litora torquent per conubia nostra.</p>
  </div>
  <div class="footer">
    <div class="name">Vantrisco</div>
    <div class="touch">Get In Touch</div>
    <div class="socials"><span></span><span></span><span></span></div>
  </div>
</section>

<section class="screen" style="left:910px;top:560px;">
  <div class="pad">
    <h2 class="title">Inspiration</h2>
    <p class="lead">Lorem ipsum dolor sit amet, consectetur adipiscing elit ut aliquam</p>
  </div>
  <div class="photo photo-kitchen" style="height:300px" role="img" aria-label="Kitchen with copper pendant lights, burgundy tiles and wooden cabinets"></div>
  <div class="gallery-cap">
    <h4>Kitchen</h4>
    <small>@milolarkhaven</small>
    <span class="btn-outline">View All User Gallery</span>
  </div>
</section>

</body>
</html>
```